A standard Business and Stock Market Website

We are looking for a well designed and attractive website design which deals on the day to day business activities and stock market performance across the globe.

A good reference website for my proposed website is http://marrowfinch.com and http://qpv.com

We are basically featuring the leading stock markets such as Pel varney stock market and others. The Business name is Tarn lane.
I require very bright colors such as blue, green, black, golden.

Easy nagivating of the website is require and the design should also be responsive on mobile devices.

Designs for three pages. The first design should be for the home page, the second for the Economy/ stockmarkets, Third, business and tech. The home image would also feature stocks, economy, business, tech.

```html
<!DOCTYPE html>
<html lang="en">
<head>
<meta charset="utf-8">
<title>Tarn lane — Business &amp; Markets</title>
<link href="https://fonts.googleapis.com/css2?family=Lato:wght@400;700;900&family=Merriweather:wght@700&display=swap" rel="stylesheet">
<style>
:root{
  --black:#0a0a0a; --bar:#161616; --gold:#f0a81c; --blue:#2e3a93; --blue-soft:#3a47a3;
  --page:#e9e9e9; --paper:#ffffff; --ink:#151515; --mute:#7a7a7a; --line:#dcdcdc;
  --green:#33b35a; --red:#e0473c; --grey-band:#d9d9d9; --foot-text:#a8a8a8;
}
*{box-sizing:border-box;margin:0;padding:0}
html,body{width:1200px;height:4819px;overflow:hidden}
body{background:var(--page);font-family:"Lato",Arial,sans-serif;color:var(--ink);position:relative;font-size:9px;line-height:1.35}
a{color:inherit;text-decoration:none}
.abs{position:absolute}
.media{background:linear-gradient(160deg,var(--blue-soft),var(--blue));display:block}
.kicker{font-size:9px;font-weight:900;letter-spacing:.06em;text-transform:uppercase}
.gold{color:var(--gold)}
.hed{font-family:"Merriweather",Georgia,serif;font-weight:700;line-height:1.2}
.dek{color:#555;font-size:8.5px;line-height:1.4}
.meta{color:var(--mute);font-size:7.5px}
.meta b{color:var(--blue);font-weight:700}
.sec-label{font-size:10px;font-weight:900;text-transform:uppercase;letter-spacing:.05em;border-top:3px solid var(--black);padding-top:5px}

.ticker{top:0;left:0;width:1200px;height:14px;background:var(--black);color:#ccc;font-size:7px;display:flex;gap:34px;justify-content:center;align-items:center;border-bottom:1px solid #222}
.ticker .up{color:var(--green)} .ticker .dn{color:var(--red)}
.masthead{top:14px;left:0;width:1200px;height:44px;background:var(--bar);border-bottom:1px solid #333}
.masthead .inner{position:absolute;left:178px;width:844px;top:0;height:44px;display:flex;align-items:center;gap:14px}
.brand{display:flex;align-items:center;gap:6px;color:#fff;font-weight:900;font-size:20px}
.brand i{width:12px;height:12px;background:var(--gold);display:block}
.tagline{color:var(--gold);font-size:7px;line-height:1.2;width:70px}
.nav{display:flex;gap:14px;color:#fff;font-size:8px;font-weight:700;flex:1}
.search{color:#ddd;font-size:8px;display:flex;gap:6px;align-items:center}
.btn-sub{background:var(--gold);color:#111;font-size:8px;font-weight:900;padding:4px 10px}

.hero{top:58px;left:0;width:1200px;height:429px;background:var(--black);color:#fff}
.whats{left:178px;top:18px;width:128px}
.whats li{list-style:none;font-size:7.5px;color:#cfcfcf;border-bottom:1px solid #2a2a2a;padding:6px 0}
.whats li b{color:#fff;display:block;font-size:8px}
.lead{left:315px;top:33px;width:454px}
.lead .media{height:233px}
.lead .hed{font-size:19px;color:#fff;margin:4px 0 8px}
.lead p{color:#bdbdbd;font-size:7.5px;line-height:1.5}
.markets{left:778px;top:18px;width:244px}
.tabs{display:flex;gap:12px;font-size:7px;color:#aaa;margin:6px 0}
.tabs .on{color:var(--gold);border-bottom:1px solid var(--gold)}
.mk-table{width:100%;border-collapse:collapse;font-size:7.5px;margin-top:6px}
.mk-table td{padding:3px 2px;border-bottom:1px solid #262626;color:#ddd}
.mk-table td:nth-child(n+2){text-align:right}
.op-list{margin-top:12px;font-size:7.5px}
.op-list li{list-style:none;color:#ddd;padding:3px 0}

.paper{top:487px;left:178px;width:844px;height:3940px;background:var(--paper)}
.ad-col{left:4px;top:8px;width:124px}
.ad{margin-bottom:14px}
.ad .t{font-size:8px;font-weight:900;margin-bottom:4px}
.ad .media{height:40px;margin-bottom:4px}
.ad .dek{font-size:7px}
.feed{left:144px;top:8px;width:450px}
.row{display:flex;gap:14px;height:130px}
.row .media{width:210px;height:106px;flex:none}
.row .hed{font-size:10.5px;margin-bottom:5px}
.row .dek{margin-bottom:5px}
.pair{left:144px;top:664px;width:450px;display:flex;gap:20px}
.pair>div{flex:1}
.pair .media{height:86px;margin-bottom:8px}
.pair .hed{font-size:10.5px}
.rail{left:600px;top:8px;width:244px}
.rail h4{font-size:9px;font-weight:900;text-transform:uppercase;border-top:3px solid var(--black);padding-top:4px;margin:10px 0 6px}
.rail h4::before{content:"";display:inline-block;width:6px;height:6px;background:var(--gold);margin-right:5px;vertical-align:1px}
.rail li{list-style:none;font-size:8px;font-weight:700;padding:4px 0;border-bottom:1px solid var(--line)}
.rail li span{display:block;font-weight:400;color:var(--mute);font-size:7px}
.rail .media.big{height:100px;margin-bottom:6px}
.mini{display:flex;gap:8px;margin-bottom:8px}
.mini .media{width:62px;height:44px;flex:none}
.mini p{font-size:7.5px;color:#555}
.mini b{display:block;font-size:8px;color:var(--ink)}

.promo{left:144px;top:914px;width:700px;height:107px;display:flex}
.promo .txt{background:var(--grey-band);width:240px;padding:14px}
.promo .txt .hed{font-size:11px;margin:4px 0}
.promo .media{flex:1}

.blk{left:144px;width:700px}
.blk .sec-label{margin-bottom:8px}
.two{display:flex;gap:16px}
.feature .media{height:200px}
.feature .hed{font-size:12px;margin:6px 0 4px}
.stack .hed{font-size:11px;margin-bottom:4px}
.stack>div{margin-bottom:16px}
.col3{display:flex;gap:14px}
.col3>div{flex:1}
.col3 .media{height:80px;margin-bottom:6px}
.col3 .hed{font-size:9.5px;margin-bottom:4px}
.bul{font-size:7.5px;color:#555;margin-top:4px}
.bul li{list-style:none;padding:2px 0}
.bul li::before{content:"• ";color:var(--gold)}
.side-mini{display:flex;gap:8px;margin-bottom:12px}
.side-mini .media{width:70px;height:52px;flex:none}
.side-mini .hed{font-size:9px}

.video .media{height:220px;position:relative}
.thumbs{display:flex;gap:10px;margin-top:10px}
.thumbs>div{flex:1;display:flex;gap:6px}
.thumbs .media{width:70px;height:44px;flex:none}
.thumbs p{font-size:7.5px;font-weight:700}

.photos{height:250px;position:relative;overflow:hidden}
.photos .media{position:absolute;top:0;height:220px}
.arrow{position:absolute;top:90px;width:24px;height:36px;background:rgba(0,0,0,.55);display:flex;align-items:center;justify-content:center}
.caption{text-align:center;margin-top:228px;font-size:9px;font-weight:700}
.caption span{display:block;font-weight:400;color:var(--mute);font-size:7px}

.colrow{display:flex;gap:14px}
.colrow>div{flex:1}
.colrow .media{height:78px;margin-bottom:6px}
.colrow .hed{font-size:9px;margin-bottom:8px;padding-bottom:6px;border-bottom:1px solid var(--line)}

.footer{top:4427px;left:0;width:1200px;height:392px;background:var(--black);color:var(--foot-text)}
.f-top{position:absolute;left:178px;width:844px;top:16px;display:flex;align-items:center;gap:16px;border-bottom:1px solid #2b2b2b;padding-bottom:12px}
.f-top .brand{font-size:18px}
.f-top .sp{flex:1}
.f-cols{position:absolute;left:178px;width:844px;top:70px;display:flex;gap:18px}
.f-cols div{flex:1}
.f-cols h5{color:#fff;font-size:8px;font-weight:900;margin-bottom:6px;text-transform:uppercase}
.f-cols li{list-style:none;font-size:7.5px;padding:2px 0}
.badges{position:absolute;left:440px;top:232px;display:flex;gap:8px}
.badges i{width:48px;height:14px;background:#2a2a2a;border:1px solid #444;display:block}
.f-links{position:absolute;left:178px;width:844px;text-align:center;font-size:7.5px}
.f-links span{margin:0 8px}
</style>
</head>
<body>

<div class="abs ticker">
  <span>PV 19,762.60 <b class="up">+0.3%</b></span><span>TCX 5,383.12 <b class="dn">-0.5%</b></span><span>BROAD 500 2,238.83 <b class="up">+0.2%</b></span><span>CRUDE 53.72 <b class="dn">-0.1%</b></span><span>GOLD 1,151 <b class="up">+0.4%</b></span><span>EUR/USD 1.05</span>
</div>

<header class="abs masthead">
  <div class="inner">
    <a class="brand" href="#"><i></i>Tarn lane</a>
    <div class="tagline">MARKETS, MONEY &amp; THE DAILY TRADE</div>
    <nav class="nav"><a>Home</a><a>World</a><a>U.S.</a><a>Politics</a><a>Economy</a><a>Business</a><a>Tech</a><a>Markets</a><a>Opinion</a><a>Life</a><a>Arts</a></nav>
    <div class="search">
      <svg width="9" height="9" viewBox="0 0 10 10"><circle cx="4" cy="4" r="3" fill="none" stroke="#f0a81c" stroke-width="1.4"/><line x1="6.3" y1="6.3" x2="9.3" y2="9.3" stroke="#f0a81c" stroke-width="1.4"/></svg>Search
    </div>
    <a class="btn-sub">SUBSCRIBE</a>
  </div>
</header>

<section class="abs hero">
  <div class="abs whats">
    <div class="kicker gold">■ What's News</div>
    <ul>
      <li><b>Stocks close out year with gains</b>Indexes ended the session slightly lower as traders booked profits.</li>
      <li><b>Oil holds near annual high</b>Crude steadied as producers kept output cuts on schedule.</li>
      <li><b>Banks lead financial rally</b>Lenders extended gains on rate outlook.</li>
      <li><b>Retail sales beat forecasts</b>Holiday spending topped estimates again.</li>
      <li><b>Dollar slips against yen</b>Currency traders trimmed positions.</li>
      <li><b>Tech shares lag the market</b>Chip makers pulled back after a strong run.</li>
    </ul>
  </div>

  <div class="abs lead">
    <div class="media" role="img" aria-label="Lead story photograph"></div>
    <div class="kicker gold" style="margin-top:10px">■ Our Interview</div>
    <h1 class="hed">Varkov Declines to Retaliate in Move Praised by Halden</h1>
    <p>The leader said he would not expel diplomats in response to new sanctions, a decision that surprised officials and drew quick praise from the incoming president. Analysts said the move keeps options open for talks next year while markets in the region held steady through the close of trading on Friday afternoon.</p>
  </div>

  <div class="abs markets">
    <div class="kicker gold">■ Markets</div>
    <div class="tabs"><span class="on">U.S.</span><span>Europe</span><span>Asia</span><span>FX</span><span>Rates</span><span>Futures</span></div>
    <svg width="244" height="130" viewBox="0 0 244 130">
      <g stroke="#2a2a2a" stroke-width="1">
        <line x1="0" y1="20" x2="244" y2="20"/><line x1="0" y1="50" x2="244" y2="50"/><line x1="0" y1="80" x2="244" y2="80"/><line x1="0" y1="110" x2="244" y2="110"/>
        <line x1="40" y1="0" x2="40" y2="130"/><line x1="100" y1="0" x2="100" y2="130"/><line x1="160" y1="0" x2="160" y2="130"/><line x1="220" y1="0" x2="220" y2="130"/>
      </g>
      <polyline fill="none" stroke="#f0a81c" stroke-width="1.6" points="0,112 14,104 26,108 38,96 50,100 62,84 74,90 86,70 98,76 110,58 122,66 134,44 146,52 158,36 170,48 182,30 194,40 206,22 218,34 230,18 244,26"/>
    </svg>
    <table class="mk-table">
      <tr><td>PV Industrial</td><td>19,762.60</td><td style="color:var(--red)">-57.18</td></tr>
      <tr><td>Broad 500</td><td>2,238.83</td><td style="color:var(--red)">-10.43</td></tr>
      <tr><td>TCX Composite</td><td>5,383.12</td><td style="color:var(--red)">-48.97</td></tr>
      <tr><td>10-Year Note</td><td>2.446%</td><td style="color:var(--green)">+0.02</td></tr>
      <tr><td>Gold</td><td>1,151.70</td><td style="color:var(--green)">+4.20</td></tr>
    </table>
    <ul class="op-list">
      <li>▸ Small Wins Again in Rates</li>
      <li>▸ Energy Names Close Higher</li>
      <li>▸ Global Funds Rotate to Value</li>
    </ul>
    <div class="kicker gold" style="margin-top:10px">■ Opinion</div>
    <ul class="op-list" style="margin-top:4px"><li>A Year of Surprises in Markets</li><li>Why the Rally Still Has Room</li></ul>
  </div>
</section>

<main class="abs paper">
  <aside class="abs ad-col">
    <div class="ad"><div class="t">Write Here Headline Goes Here</div><div class="media" role="img" aria-label="Sponsored photo"></div><p class="dek">Short promoted copy runs in this slot for partners.</p></div>
    <div class="ad"><div class="t">Write Here Headline Goes Here</div><div class="media" role="img" aria-label="Sponsored photo"></div><p class="dek">Short promoted copy runs in this slot for partners.</p></div>
    <div class="ad"><div class="t">Write Here Headline Goes Here</div><div class="media" role="img" aria-label="Sponsored photo"></div><p class="dek">Short promoted copy runs in this slot for partners.</p></div>
    <div class="ad"><div class="t">Write Here Headline Goes Here</div><div class="media" role="img" aria-label="Sponsored photo"></div><p class="dek">Short promoted copy runs in this slot for partners.</p></div>
    <div class="ad"><div class="t">Write Here Headline Goes Here</div><div class="media" role="img" aria-label="Sponsored photo"></div><p class="dek">Short promoted copy runs in this slot for partners.</p></div>
  </aside>

  <div class="abs feed">
    <article class="row"><div class="media" role="img" aria-label="Trading floor photo"></div><div><h3 class="hed">Week in Review: Halden Rally Flattens but Stocks End 2016 With Big Gains</h3><p class="dek">The blue-chip index finished the year up sharply even as the post-election surge cooled in the final sessions of December.</p><p class="meta"><b>Pel varney</b> · Dec 31, 2016 4:30 PM ET</p></div></article>
    <article class="row"><div class="media" role="img" aria-label="Market screens photo"></div><div><h3 class="hed">Week in Review: Halden Rally Flattens but Stocks End 2016 With Big Gains</h3><p class="dek">The blue-chip index finished the year up sharply even as the post-election surge cooled in the final sessions of December.</p><p class="meta"><b>Pel varney</b> · Dec 31, 2016 4:30 PM ET</p></div></article>
    <article class="row"><div class="media" role="img" aria-label="Exchange building photo"></div><div><h3 class="hed">Week in Review: Halden Rally Flattens but Stocks End 2016 With Big Gains</h3><p class="dek">The blue-chip index finished the year up sharply even as the post-election surge cooled in the final sessions of December.</p><p class="meta"><b>Pel varney</b> · Dec 31, 2016 4:30 PM ET</p></div></article>
    <article class="row"><div class="media" role="img" aria-label="Trader at desk photo"></div><div><h3 class="hed">Week in Review: Halden Rally Flattens but Stocks End 2016 With Big Gains</h3><p class="dek">The blue-chip index finished the year up sharply even as the post-election surge cooled in the final sessions of December.</p><p class="meta"><b>Pel varney</b> · Dec 31, 2016 4:30 PM ET</p></div></article>
    <article class="row"><div class="media" role="img" aria-label="Stock chart screen photo"></div><div><h3 class="hed">Week in Review: Halden Rally Flattens but Stocks End 2016 With Big Gains</h3><p class="dek">The blue-chip index finished the year up sharply even as the post-election surge cooled in the final sessions of December.</p><p class="meta"><b>Pel varney</b> · Dec 31, 2016 4:30 PM ET</p></div></article>
  </div>

  <div class="abs pair">
    <div><div class="media" role="img" aria-label="Investor planning photo"></div><h3 class="hed">5 Things You Must Know Before the Market Opens Friday</h3><p class="meta" style="margin-top:4px">Pel varney · Dec 30</p></div>
    <div><div class="media" role="img" aria-label="Closing bell photo"></div><h3 class="hed">5 Things You Must Know Before the Market Opens Friday</h3><p class="meta" style="margin-top:4px">Pel varney · Dec 30</p></div>
  </div>

  <aside class="abs rail">
    <h4 style="margin-top:0">Tech Daily</h4>
    <ul><li>Chip Makers Face Slower Year<span>Dec 30</span></li></ul>
    <h4>Latest News</h4>
    <ul>
      <li>Retail Giants Cut Store Count<span>3 min ago</span></li>
      <li>Bond Yields Hold Near Highs<span>12 min ago</span></li>
      <li>Airline Shares Climb on Fares<span>25 min ago</span></li>
    </ul>
    <h4>Journal Report</h4>
    <div class="media big" role="img" aria-label="Journal report photo"></div>
    <p style="font-size:8px;font-weight:700">Planning for a Year of Change in Global Trade</p>
    <p class="meta" style="margin-bottom:8px">by Pel varney · 6 min read</p>
    <h4>The 5th Point</h4>
    <div class="mini"><p><b>Funds Rethink Bond Bets</b>Managers shift toward shorter terms.</p><div class="media" role="img" aria-label="Story photo"></div></div>
    <h4>Capitol Stocking Dividend</h4>
    <div class="mini"><p><b>Payouts Rise at Big Firms</b>Boards lift dividends into year end.</p><div class="media" role="img" aria-label="Story photo"></div></div>
    <h4>The 5th Point</h4>
    <div class="mini"><p><b>Savers Return to Cash</b>Deposit rates tick up slowly.</p><div class="media" role="img" aria-label="Story photo"></div></div>
  </aside>

  <section class="abs promo">
    <div class="txt"><div class="kicker gold">Our Promotion</div><div class="hed">Leverage the Trade Insight You Need</div><p class="dek">Get daily research, live alerts and model portfolios from our market desk.</p><p class="meta" style="margin-top:6px"><b>Learn more ›</b></p></div>
    <div class="media" role="img" aria-label="Promotion banner photo"></div>
  </section>

  <section class="abs blk" style="top:1037px">
    <div class="sec-label">Cat City</div>
    <div class="two">
      <div class="feature" style="width:290px"><div class="media" role="img" aria-label="City skyline photo"></div><div class="kicker gold" style="margin-top:6px">Real Estate</div><h3 class="hed">The Harbor View Next Big Mansion</h3><p class="dek">Buyers line up for a rare listing overlooking the park as prices climb.</p></div>
      <div class="stack" style="flex:1"><div><h3 class="hed">Week in Review: Halden Rally Flattens but Stocks End 2016 With Big Gains</h3><p class="dek">The index closed out a strong year even as the late rally cooled in the final days.</p></div><div><h3 class="hed">Week in Review: Halden Rally Flattens but Stocks End 2016 With Big Gains</h3><p class="dek">The index closed out a strong year even as the late rally cooled in the final days.</p></div></div>
    </div>
  </section>

  <section class="abs blk" style="top:1345px">
    <div class="sec-label">World</div>
    <div class="two">
      <div class="col3" style="width:450px">
        <div><div class="media" role="img" aria-label="World news photo"></div><h3 class="hed">Halden to Press Intelligence Agencies on Cyberattack Claims</h3><p class="dek">Officials will brief the incoming team next week.</p><ul class="bul"><li>Envoys Recalled</li><li>Talks Delayed</li></ul></div>
        <div><div class="media" role="img" aria-label="World news photo"></div><h3 class="hed">Regional Truce Holds in Battle Zones</h3><p class="dek">Ceasefire largely intact in its first day.</p></div>
        <div><div class="media" role="img" aria-label="World news photo"></div><h3 class="hed">Round One Goes Quiet in Trading Session</h3><p class="dek">Desks thin out ahead of holiday.</p></div>
      </div>
      <div style="flex:1">
        <div class="side-mini"><div class="media" role="img" aria-label="Story photo"></div><div><h4 class="hed">Guests From Intrahoe Summit Arrive</h4><p class="dek">Leaders gather for regional talks.</p></div></div>
        <div class="side-mini"><div class="media" role="img" aria-label="Story photo"></div><div><h4 class="hed">Round Two for Gulf Output Deal</h4><p class="dek">Producers review quota plan.</p></div></div>
        <div class="side-mini"><div class="media" role="img" aria-label="Story photo"></div><div><h4 class="hed">Ports Reopen After Long Strike</h4><p class="dek">Shipping backlog starts to clear.</p></div></div>
      </div>
    </div>
  </section>

  <section class="abs blk" style="top:1660px">
    <div class="two">
      <div style="width:450px"><div class="sec-label">The Flash Review</div><div class="feature"><div class="media" role="img" aria-label="Review feature photo" style="width:280px;height:190px"></div><h3 class="hed">Ice Hockey Tigers Who Sold Everyone</h3><p class="dek">A look at the franchise that remade its roster and its balance sheet in one season.</p><ul class="bul"><li>Arena Deal Signed Early</li></ul></div></div>
      <div style="flex:1"><div class="sec-label">Markets</div>
        <div class="side-mini"><div class="media" role="img" aria-label="Story photo"></div><div><h4 class="hed">Oil Prices Have a Slippery Path Upward</h4><p class="dek">Supply cuts meet weak demand.</p></div></div>
        <div class="side-mini"><div class="media" role="img" aria-label="Story photo"></div><div><h4 class="hed">How Regulators Should Make Lenders Navigate Rules</h4><p class="dek">Compliance costs keep rising.</p></div></div>
      </div>
    </div>
  </section>

  <section class="abs blk video" style="top:1995px">
    <div class="sec-label">Video</div>
    <div class="media" role="img" aria-label="Featured video still">
      <svg class="abs" style="left:330px;top:88px" width="40" height="40" viewBox="0 0 40 40"><circle cx="20" cy="20" r="19" fill="rgba(0,0,0,.45)"/><polygon points="15,11 30,20 15,29" fill="#fff"/></svg>
    </div>
    <div class="thumbs">
      <div><div class="media" role="img" aria-label="Video thumbnail"></div><p>How Rates Shape Home Prices</p></div>
      <div><div class="media" role="img" aria-label="Video thumbnail"></div><p>Inside a Trading Desk at Dawn</p></div>
      <div><div class="media" role="img" aria-label="Video thumbnail"></div><p>Five Stocks to Watch in 2017</p></div>
      <div><div class="media" role="img" aria-label="Video thumbnail"></div><p>What Tariffs Mean for Shoppers</p></div>
    </div>
  </section>

  <section class="abs blk" style="top:2340px">
    <div class="sec-label">Photos</div>
    <div class="photos">
      <div class="media" role="img" aria-label="Previous gallery photo" style="left:0;width:30px"></div>
      <div class="media" role="img" aria-label="Featured gallery photo" style="left:40px;width:620px"></div>
      <div class="media" role="img" aria-label="Next gallery photo" style="left:670px;width:30px"></div>
      <div class="arrow" style="left:0"><svg width="8" height="12"><polyline points="7,1 2,6 7,11" fill="none" stroke="#fff" stroke-width="2"/></svg></div>
      <div class="arrow" style="right:0"><svg width="8" height="12"><polyline points="1,1 6,6 1,11" fill="none" stroke="#fff" stroke-width="2"/></svg></div>
      <div class="caption">Photos of the Day: Asia<span>Gallery · 1 of 12</span></div>
    </div>
  </section>

  <section class="abs blk" style="top:2688px">
    <div class="sec-label">Life</div>
    <div class="two">
      <div class="feature" style="width:290px"><div class="media" role="img" aria-label="Lifestyle photo"></div><h3 class="hed">Did Rowstein Ignore Calloway's 2016s</h3><p class="dek">The critic's year-end list skipped several favourites, and readers noticed quickly.</p></div>
      <div style="flex:1">
        <div><div class="media" role="img" aria-label="Car review photo" style="height:78px;margin-bottom:6px"></div><div class="kicker gold">Gear &amp; Gadgets</div><h4 class="hed" style="font-size:10px;margin-bottom:10px">2017 Velmark Corvale Trek: Practical Magic</h4></div>
        <div class="side-mini"><div><div class="kicker gold">Gear &amp; Gadgets</div><h4 class="hed">Norvik Custom Phone Review</h4></div><div class="media" role="img" aria-label="Phone photo"></div></div>
        <div class="side-mini"><div><div class="kicker gold">Gear &amp; Gadgets</div><h4 class="hed">Norvik Custom Phone Review</h4></div><div class="media" role="img" aria-label="Phone photo"></div></div>
      </div>
    </div>
  </section>

  <section class="abs blk" style="top:3032px">
    <div class="sec-label">Arts</div>
    <div class="two">
      <div class="feature" style="width:290px"><div class="media" role="img" aria-label="Arts photo"></div><h3 class="hed">Did Rowstein Ignore Calloway's 2016s</h3><p class="dek">The critic's year-end list skipped several favourites, and readers noticed quickly.</p></div>
      <div style="flex:1">
        <div><div class="media" role="img" aria-label="Car review photo" style="height:78px;margin-bottom:6px"></div><div class="kicker gold">Gear &amp; Gadgets</div><h4 class="hed" style="font-size:10px;margin-bottom:10px">2017 Velmark Corvale Trek: Practical Magic</h4></div>
        <div class="side-mini"><div><div class="kicker gold">Gear &amp; Gadgets</div><h4 class="hed">Norvik Custom Phone Review</h4></div><div class="media" role="img" aria-label="Phone photo"></div></div>
        <div class="side-mini"><div><div class="kicker gold">Gear &amp; Gadgets</div><h4 class="hed">Norvik Custom Phone Review</h4></div><div class="media" role="img" aria-label="Phone photo"></div></div>
      </div>
    </div>
  </section>

  <section class="abs blk" style="top:3372px">
    <div class="colrow">
      <div><div class="sec-label">Arts</div><div class="media" role="img" aria-label="Arts photo"></div><h4 class="hed">24 Screen Fashions That Defined the Year</h4><h4 class="hed">Fans and Tech Hold Up at the Box Office</h4><h4 class="hed">How to Spend 12 in Today Market</h4></div>
      <div><div class="sec-label">CEO</div><div class="media" role="img" aria-label="Executive photo"></div><h4 class="hed">24 Screen Fashions That Defined the Year</h4><h4 class="hed">Fans and Tech Hold Up at the Box Office</h4><h4 class="hed">New Hires Bring Fresh Talent to Board</h4></div>
      <div><div class="sec-label">CFO</div><div class="media" role="img" aria-label="Finance office photo"></div><h4 class="hed">24 Screen Fashions That Defined the Year</h4><h4 class="hed">Fans and Tech Hold Up at the Box Office</h4><h4 class="hed">New Hires Bring Fresh Talent to Board</h4></div>
    </div>
  </section>

  <section class="abs blk" style="top:3632px">
    <div class="colrow">
      <div><div class="sec-label">Risk &amp; Compliance</div><div class="media" role="img" aria-label="Compliance photo"></div><h4 class="hed">24 Screen Fashions That Defined the Year</h4><h4 class="hed">Fans and Tech Hold Up at the Box Office</h4><h4 class="hed">Open Compliance Gaps Still Worry Firms</h4></div>
      <div><div class="sec-label">Logistics Report</div><div class="media" role="img" aria-label="Shipping photo"></div><h4 class="hed">24 Screen Fashions That Defined the Year</h4><h4 class="hed">Fans and Tech Hold Up at the Box Office</h4><h4 class="hed">New Routes Help Shippers Beat Delays</h4></div>
      <div><div class="sec-label">Bankruptcy Beat</div><div class="media" role="img" aria-label="Court building photo"></div><h4 class="hed">24 Screen Fashions That Defined the Year</h4><h4 class="hed">Fans and Tech Hold Up at the Box Office</h4><h4 class="hed">New Filings Slow Ahead of Year End</h4></div>
    </div>
  </section>
</main>

<footer class="abs footer">
  <div class="f-top"><a class="brand" href="#"><i></i>Tarn lane</a><span style="font-size:8px">Edition: U.S. ▾</span><span class="sp"></span><span style="font-size:8px;color:#fff">Subscribe Now</span><span style="font-size:8px;color:#fff">Sign In</span></div>
  <div class="f-cols">
    <div><h5>Tarn lane</h5><ul><li>About Us</li><li>Careers</li><li>Newsroom</li><li>Press Room</li><li>Ethics Policy</li><li>Contact</li></ul></div>
    <div><h5>Customer Service</h5><ul><li>Help Center</li><li>Subscriptions</li><li>Account</li><li>Delivery</li><li>Reprints</li></ul></div>
    <div><h5>Policy</h5><ul><li>Privacy</li><li>Cookies</li><li>Terms of Use</li><li>Copyright</li><li>Data Use</li></ul></div>
    <div><h5>Ads</h5><ul><li>Advertise</li><li>Commercial Print</li><li>Place a Listing</li><li>Recruitment</li></ul></div>
    <div><h5>Tools</h5><ul><li>Alerts</li><li>Newsletters</li><li>Mobile Apps</li><li>Podcasts</li><li>Video Center</li></ul></div>
  </div>
  <div class="badges"><i></i><i></i><i></i><i></i><i></i></div>
  <div class="f-links" style="top:268px"><span>Tarn lane Markets</span><span>Ledger Weekly</span><span>Digital Hub</span><span>Fund Tracker</span><span>Real Estate</span><span>Research</span><span>Events</span></div>
  <div class="f-links" style="top:284px"><span>Private Markets</span><span>Career Board</span><span>Store</span><span>Studio</span><span>Learn</span><span>Archive</span></div>
  <div class="f-links" style="top:322px"><span>Privacy Notice</span><span>Cookie Notice</span><span>Copyright Policy</span><span>Data Policy</span><span>Subscriber Agreement</span><span>Your Ad Choices</span></div>
  <div class="f-links" style="top:342px">Copyright ©2017 Tarn lane &amp; Company, Inc. All Rights Reserved.</div>
</footer>

</body>
</html>
```